Brookvale Holdings Ltd - Logo and Business Card

Create a logo and business card design for our new company.

Canadian private investment company with holdings in Saskatchewan Oil and real-estate.

Target Market(s)

Investors

Industry/Entity Type

Finance

Contact Information for Business Card

Name - Dominic Harlow
Position - President
Phone - 306.482.7159
Website - www.brookvaleholdings.ca

Logo Text

Today. Tomorrow. Together. (Tag Line)

Colors

Designer to choose colors to be used in the design.

Requirements
Must have
• Logo Must Have - Type Font only
• Must be modern, professional and stand out from the crowd.
Nice to have
• Don't have any, blank slate.

```html
<!DOCTYPE html>
<html lang="en">
<head>
<meta charset="UTF-8">
<title>Brookvale Holdings – Business Card</title>
<link href="https://fonts.googleapis.com/css2?family=Arimo:wght@400;700&display=swap" rel="stylesheet">
<style>
  :root {
    --stage: #e9e6e1;
    --navy-top: #0a6494;
    --navy-bottom: #0a4670;
    --brand-light: #8fbccf;
    --brand-dark: #2d6282;
    --name-ink: #274863;
    --muted: #8f979e;
    --body-ink: #4d5258;
    --paper: #ffffff;
  }
  * { margin: 0; padding: 0; box-sizing: border-box; }
  html, body { width: 1200px; height: 1023px; overflow: hidden; }
  body {
    background: var(--stage);
    font-family: "Arimo", Arial, sans-serif;
    position: relative;
  }
  .card {
    position: absolute;
    width: 560px;
    height: 320px;
    border-radius: 18px;
    box-shadow: 0 6px 18px rgba(0,0,0,0.18);
    overflow: hidden;
  }
  .card--front {
    left: 320px; top: 130px;
    background: linear-gradient(160deg, var(--navy-top), var(--navy-bottom));
    display: flex; align-items: center; justify-content: center; gap: 18px;
  }
  .front-mark {
    width: 26px; height: 26px;
    background: var(--brand-light);
  }
  .front-name {
    color: var(--brand-light);
    font-size: 34px;
    font-weight: 400;
    letter-spacing: 1px;
  }
  .card--back {
    left: 320px; top: 573px;
    background: var(--paper);
    padding: 34px 40px;
  }
  .back-brand {
    display: flex; align-items: center; gap: 10px;
    position: absolute; right: 40px; top: 36px;
  }
  .back-mark { width: 16px; height: 16px; background: var(--brand-dark); }
  .back-name {
    color: var(--brand-dark);
    font-size: 18px; font-weight: 400; letter-spacing: 0.5px;
  }
  .person-name {
    color: var(--name-ink);
    font-size: 22px; font-weight: 400;
    margin-top: 2px;
  }
  .person-role {
    color: var(--muted);
    font-size: 14px;
    margin-top: 4px;
  }
  .contact-list {
    list-style: none;
    margin-top: 22px;
  }
  .contact-list li {
    display: flex; align-items: center; gap: 10px;
    color: var(--body-ink);
    font-size: 13px;
    line-height: 24px;
  }
  .contact-list svg { width: 13px; height: 13px; flex: none; }
</style>
</head>
<body>
  <section class="card card--front" aria-label="Card front">
    <span class="front-mark"></span>
    <span class="front-name">Brookvale Holdings</span>
  </section>

  <section class="card card--back" aria-label="Card back">
    <div class="back-brand">
      <span class="back-mark"></span>
      <span class="back-name">Brookvale Holdings</span>
    </div>
    <h1 class="person-name">Dominic Harlow</h1>
    <p class="person-role">President</p>
    <ul class="contact-list">
      <li>
        <svg viewBox="0 0 12 12"><path d="M6 0.5a4 4 0 0 1 4 4c0 3-4 7-4 7s-4-4-4-7a4 4 0 0 1 4-4z" fill="#4d5258"/><circle cx="6" cy="4.5" r="1.4" fill="#fff"/></svg>
        Your address
      </li>
      <li>
        <svg viewBox="0 0 12 12"><circle cx="6" cy="6" r="5.2" fill="none" stroke="#4d5258" stroke-width="1.1"/><path d="M4.2 3.4l1 1-.6.7c.4.9 1 1.5 1.9 1.9l.7-.6 1 1-.8.9c-2-.4-3.6-2-4-4z" fill="#4d5258"/></svg>
        306.482.7159
      </li>
      <li>
        <svg viewBox="0 0 12 12"><rect x="0.8" y="2.3" width="10.4" height="7.4" fill="none" stroke="#4d5258" stroke-width="1.1"/><path d="M1 2.6l5 4 5-4" fill="none" stroke="#4d5258" stroke-width="1.1"/></svg>
        info@brookvaleholdings.ca
      </li>
      <li>
        <svg viewBox="0 0 12 12"><circle cx="6" cy="6" r="5.2" fill="none" stroke="#4d5258" stroke-width="1.1"/><ellipse cx="6" cy="6" rx="2.2" ry="5.2" fill="none" stroke="#4d5258" stroke-width="0.9"/><path d="M0.8 6h10.4" stroke="#4d5258" stroke-width="0.9"/></svg>
        www.brookvaleholdings.ca
      </li>
    </ul>
  </section>
</body>
</html>
```